Nutritionist and Personal Chef Services Flyer. My style is clean and contemporary.

I'm looking for a clean and stylish flyer that may or may not list my services and/or prices. These flyers will be featured in southern california (orange county and los angeles) fitness centers, wellness clinics, doctors offices, restaurants etc. so it has to be appropriate for any kind of facility. I want the concept design to be similar to my website:

www.verdantplatestudio.com

This is very important! Also, please see attached file to see what my header and business cards look like to keep style and formatting consistent.
Thanks so much!

The dimensions are going to be 5.5" by 8.5" vertical. I'd like it to be double-sided with a picture on one side and my information on the other side. For the photo side, I like the idea of having the picture of the hands and cutting board (fine for this to run horizontal). On the information side I need it to address the following:

1. I'd like to have a small photo of myself. I will upload which photo I want.
2. I want my header with my font and the kiwi exactly as is. Please see attachment and keep that formatting exactly.
3. Specialty Services:
Sports Nutrition
Weight-loss
Anti-aging and Detoxification
Cancer Prevention, Management and Survivorship
Children's Health and Wellness
Specialty Diets

4. My contact info:
Marisa Quenby, C.N. NC
949-555-0186
verdantplatestudio@mailvane.com

5. My website and the FB logo

6. Call or email me today to schedule a free 30-minute consultation.

```html
<!DOCTYPE html>
<html lang="en">
<head>
<meta charset="utf-8">
<title>Verdant Plate Studio – Flyer</title>
<link rel="stylesheet" href="https://fonts.googleapis.com/css2?family=Roboto+Slab:wght@400;600&family=Source+Sans+3:wght@400;600;700&display=swap">
<style>
  :root {
    --green: #7cb342;
    --ink: #2b2b2b;
    --muted: #555555;
    --charcoal: #333333;
    --white: #ffffff;
    --backdrop: #e4e6e8;
    --rule: #d6d6d6;
  }
  * { box-sizing: border-box; margin: 0; padding: 0; }
  html, body { width: 1200px; height: 1000px; overflow: hidden; }
  body { background: var(--backdrop); font-family: "Source Sans 3", Arial, sans-serif; color: var(--ink); position: relative; }

  .brand { text-align: center; }
  .brand-name { font-family: "Source Sans 3", Arial, sans-serif; font-weight: 600; font-size: 24px; color: var(--ink); line-height: 1.1; }
  .brand-tag { font-family: "Source Sans 3", Arial, sans-serif; font-size: 13px; color: var(--muted); margin-top: 4px; letter-spacing: .4px; }

  /* Letterhead strip */
  .letterhead { position: absolute; left: 150px; top: 110px; width: 390px; height: 90px; background: var(--white); border: 1px solid var(--rule); display: flex; align-items: center; justify-content: center; }

  /* Info side */
  .flyer { position: absolute; width: 460px; height: 711px; background: var(--white); box-shadow: 0 4px 14px rgba(0,0,0,.25); overflow: hidden; }
  .flyer-info { left: 150px; top: 262px; display: flex; flex-direction: column; }
  .photo-strip { height: 72px; background: linear-gradient(90deg, #c8462e 0%, #e6dccb 30%, #d9c7a6 60%, #b9a27f 100%); border-top: 8px solid var(--green); }
  .info-header { height: 98px; display: flex; align-items: center; justify-content: center; border-bottom: 1px solid var(--rule); }
  .services { background: var(--green); color: var(--white); padding: 20px 40px 22px; height: 196px; }
  .services h2 { font-family: "Roboto Slab", Georgia, serif; font-weight: 400; font-size: 21px; margin-bottom: 10px; }
  .services ul { list-style: none; }
  .services li { display: flex; align-items: center; gap: 8px; font-size: 14.5px; line-height: 22px; }
  .services li svg { flex: none; }
  .contact { height: 240px; display: flex; }
  .portrait { width: 196px; background: linear-gradient(160deg, #8a7a6a 0%, #c9b9a4 45%, #4b3e36 100%); }
  .contact-details { flex: 1; padding: 22px 0 0 24px; }
  .contact-name { font-family: "Roboto Slab", Georgia, serif; font-weight: 600; font-size: 16px; margin-bottom: 18px; }
  .contact-name span { font-weight: 400; }
  .contact-row { display: flex; align-items: center; gap: 10px; font-size: 12px; font-weight: 600; margin-bottom: 14px; }
  .contact-row.phone { font-size: 14px; }
  .social { width: 30px; height: 30px; border-radius: 50%; background: var(--green); margin: 14px 0 0 86px; }
  .cta { flex: 1; background: var(--charcoal); color: var(--white); font-size: 17px; line-height: 22px; padding: 26px 40px 0; }
  .cta strong { font-weight: 700; }

  /* Photo side */
  .flyer-photo { left: 650px; top: 60px; display: flex; flex-direction: column; border-top: 9px solid var(--green); }
  .photo-header { height: 104px; display: flex; align-items: center; justify-content: center; border-bottom: 1px solid var(--rule); }
  .hero-photo { flex: 1; background: radial-gradient(ellipse at 40% 30%, #8bbf4a 0%, #e9e4d6 35%, #d8c8a8 60%, #f2efe8 100%); }
  .site-bar { height: 74px; background: var(--green); color: var(--white); font-size: 19px; display: flex; align-items: center; justify-content: center; letter-spacing: .3px; }
</style>
</head>
<body>

<div class="letterhead">
  <div class="brand">
    <div class="brand-name">Verdant Plate Studio</div>
    <div class="brand-tag">Nutrition Designs | Personal Chef Services</div>
  </div>
</div>

<section class="flyer flyer-info">
  <div class="photo-strip" role="img" aria-label="Photo of hands slicing mushrooms and peppers on a cutting board"></div>
  <header class="info-header">
    <div class="brand">
      <div class="brand-name">Verdant Plate Studio</div>
      <div class="brand-tag">Nutrition Designs | Personal Chef Services</div>
    </div>
  </header>
  <div class="services">
    <h2>Specialty Services:</h2>
    <ul>
      <li><svg width="13" height="13" viewBox="0 0 13 13"><circle cx="6.5" cy="6.5" r="5.6" fill="none" stroke="#fff" stroke-width="1.3"/><path d="M3.8 6.6l1.9 1.9 3.5-3.6" fill="none" stroke="#fff" stroke-width="1.4"/></svg>Sports Nutrition</li>
      <li><svg width="13" height="13" viewBox="0 0 13 13"><circle cx="6.5" cy="6.5" r="5.6" fill="none" stroke="#fff" stroke-width="1.3"/><path d="M3.8 6.6l1.9 1.9 3.5-3.6" fill="none" stroke="#fff" stroke-width="1.4"/></svg>Weight-loss</li>
      <li><svg width="13" height="13" viewBox="0 0 13 13"><circle cx="6.5" cy="6.5" r="5.6" fill="none" stroke="#fff" stroke-width="1.3"/><path d="M3.8 6.6l1.9 1.9 3.5-3.6" fill="none" stroke="#fff" stroke-width="1.4"/></svg>Anti-aging and Detoxification</li>
      <li><svg width="13" height="13" viewBox="0 0 13 13"><circle cx="6.5" cy="6.5" r="5.6" fill="none" stroke="#fff" stroke-width="1.3"/><path d="M3.8 6.6l1.9 1.9 3.5-3.6" fill="none" stroke="#fff" stroke-width="1.4"/></svg>Cancer Prevention, Management and Survivorship</li>
      <li><svg width="13" height="13" viewBox="0 0 13 13"><circle cx="6.5" cy="6.5" r="5.6" fill="none" stroke="#fff" stroke-width="1.3"/><path d="M3.8 6.6l1.9 1.9 3.5-3.6" fill="none" stroke="#fff" stroke-width="1.4"/></svg>Children's Health and Wellness</li>
      <li><svg width="13" height="13" viewBox="0 0 13 13"><circle cx="6.5" cy="6.5" r="5.6" fill="none" stroke="#fff" stroke-width="1.3"/><path d="M3.8 6.6l1.9 1.9 3.5-3.6" fill="none" stroke="#fff" stroke-width="1.4"/></svg>Specialty Diets</li>
    </ul>
  </div>
  <div class="contact">
    <div class="portrait" role="img" aria-label="Portrait of the nutritionist preparing vegetables in her kitchen"></div>
    <div class="contact-details">
      <div class="contact-name">Marisa Quenby, <span>C.N. NC</span></div>
      <div class="contact-row phone">
        <svg width="14" height="20" viewBox="0 0 14 20"><rect x="1" y="1" width="12" height="18" rx="2" fill="var(--green)"/><rect x="3" y="3.5" width="8" height="10" fill="#fff"/><circle cx="7" cy="16.3" r="1.2" fill="#fff"/></svg>
        949-555-0186
      </div>
      <div class="contact-row">
        <svg width="16" height="12" viewBox="0 0 16 12"><rect x="0.5" y="0.5" width="15" height="11" fill="var(--green)"/><path d="M1 1l7 6 7-6" fill="none" stroke="#fff" stroke-width="1.2"/></svg>
        verdantplatestudio@mailvane.com
      </div>
      <div class="contact-row">
        <svg width="15" height="15" viewBox="0 0 15 15"><circle cx="7.5" cy="7.5" r="6.5" fill="var(--green)"/><path d="M1 7.5h13M7.5 1c-3 3.5-3 9.5 0 13M7.5 1c3 3.5 3 9.5 0 13" fill="none" stroke="#fff" stroke-width="1"/></svg>
        www.verdantplatestudio.com
      </div>
      <div class="social" role="img" aria-label="Social media link"></div>
    </div>
  </div>
  <footer class="cta"><strong>Call</strong> or <strong>email</strong> me today to schedule a <strong>free</strong><br>15-minute consultation.</footer>
</section>

<section class="flyer flyer-photo">
  <header class="photo-header">
    <div class="brand">
      <div class="brand-name">Verdant Plate Studio</div>
      <div class="brand-tag">Nutrition Designs | Personal Chef Services</div>
    </div>
  </header>
  <div class="hero-photo" role="img" aria-label="Photo of hands slicing mushrooms on a wooden cutting board with lettuce, red peppers and brussels sprouts"></div>
  <footer class="site-bar">www.verdantplatestudio.com</footer>
</section>

</body>
</html>
```